Design the Mobile Version of Existing Web Based Health Platform

Loomcrest is a social business enterprise that focus on public health by applying innovative healthcare services and consumer internet technology. Loomcrest offers a personalized platform of health promotion and disease prevention that puts the individual back in control of his life.

Loomcrest is looking for a Mobile Web UX/Visual Design professional to create a mobile version of Loomcrest website platform for iPhone, iPad/tablet and Android.

Contestants must to check www.loomcrest-demo.com.br to have a better understanding of Loomcrest Platform by creating an account (it's in portuguese, but anyone can get the general idea).

The mobile version of Loomcrest should have very similar functionality and user flows. This job is not to reengineer or re-imagine Loomcrest. It is just to reformat the existing functionality so it works well on mobile devices.

This description below is to help you to understand the core features of the platform (check the attachments to see the new web design of each one):

- Personally Controlled Health Record - PCHR enables an individual to own and manage a complete, secure, digital copy of her health and wellness information.
- Health Risk Assessments - is a process to estimate the nature and probability of adverse health effects, based on personal and family historical data, behavior and environment.
- Simulation of future health - "what if analysis" that emphasizes health education and behavior change.
- Step Quests - a program that gives you the opportunity to the participant to advance his personal well-being by doing simple Step Quests
- Health Alerts and Recommendations and Missing Data - Recommendations based on Wellbeing Bureau Guidelines and Federal Wellness Review Panel (FWRP), plus notifications to update outdated information.

The deliverable for this project is a psd file with a designed mobile version of Loomcrest.

A new design of the web platform is under construction. You can also check it looking at the files attached.

Target Market(s)

people 25-40 years old, 60% female, socially engaged

Industry/Entity Type

Healthcare

Requirements
Must have
• iPhone, iPad and Android version

Design must cover all current functionalities available on the web version (please, ensure you understand all features by creating an account at www.loomcrest-demo.com.br)

- Login/Sign up
- Welcome (first assessment)
- Add to Personal Controlled Health Record (PCHR)
- Update/Remove PCHR
- List PCHR
- Riskgrid (risk assessmen results)
- Simulation
- Alerts
- Missing data
- Recommendations
- StepQuest
- Badges
- Configurations

It's important to check the attachments to see how the web platform design is evolving.

```html
<!DOCTYPE html>
<html lang="en">
<head>
<meta charset="utf-8">
<title>Loomcrest – Add Record</title>
<link rel="stylesheet" href="https://fonts.googleapis.com/css2?family=Roboto:wght@300;400;500;700&display=swap">
<style>
  :root {
    --status-bg: #000000;
    --status-text: #ffffff;
    --header-green: #8fcb3c;
    --header-green-light: #a6d957;
    --back-green: #76b52a;
    --page-bg: #e9ecf1;
    --card-bg: #ffffff;
    --card-edge: #d7dbe2;
    --select-bg: #a5acbd;
    --select-edge: #8f97aa;
    --label: #6c6f75;
    --hint: #8a8d93;
    --input-edge: #c9ccd2;
    --addon-bg: #f3f4f6;
    --placeholder: #a0a3a8;
    --button-green: #8dc63f;
    --button-green-dark: #7cb332;
    --white: #ffffff;
  }
  * { box-sizing: border-box; margin: 0; padding: 0; }
  html, body { width: 677px; height: 1200px; overflow: hidden; }
  body {
    font-family: "Roboto", "Helvetica Neue", Arial, sans-serif;
    background: var(--page-bg);
    position: relative;
  }
  .status-bar {
    position: absolute; left: 0; top: 0; width: 677px; height: 45px;
    background: var(--status-bg); color: var(--status-text);
    font-size: 24px; font-weight: 400;
  }
  .status-bar .carrier { position: absolute; left: 10px; top: 8px; display: flex; align-items: center; gap: 8px; }
  .status-bar .time { position: absolute; left: 0; right: 0; top: 8px; text-align: center; font-weight: 500; }
  .status-bar .battery { position: absolute; right: 10px; top: 8px; display: flex; align-items: center; gap: 8px; }

  .app-header {
    position: absolute; left: 0; top: 45px; width: 677px; height: 95px;
    background: linear-gradient(var(--header-green-light), var(--header-green));
  }
  .back-button {
    position: absolute; left: 0; top: 0; width: 100px; height: 95px;
    background: var(--back-green);
    display: flex; align-items: center; justify-content: center;
  }
  .app-header h1 {
    position: absolute; left: 0; right: 0; top: 0; line-height: 95px;
    text-align: center; color: var(--white); font-size: 41px; font-weight: 700;
  }

  .intro {
    position: absolute; left: 0; right: 0; top: 162px;
    text-align: center; color: var(--hint); font-size: 27px; font-weight: 300; line-height: 34px;
  }

  .record-card {
    position: absolute; left: 32px; top: 260px; width: 613px; height: 602px;
    background: var(--card-bg); border: 1px solid var(--card-edge);
    box-shadow: 0 4px 0 #d3d7de;
  }
  .category-select {
    position: absolute; left: 92px; top: 74px; width: 436px; height: 83px;
    background: var(--select-bg); border: 2px solid var(--select-edge); border-radius: 4px;
    color: var(--white); font-size: 31px; font-weight: 400;
    display: flex; align-items: center; justify-content: center;
  }
  .category-select svg { position: absolute; right: 24px; top: 30px; }
  .field-label {
    position: absolute; left: 0; right: 0; text-align: center;
    color: var(--label); font-size: 28px; font-weight: 300;
  }
  .text-field {
    position: absolute; left: 92px; width: 440px; height: 84px;
    border: 2px solid var(--input-edge); border-radius: 6px; background: var(--white);
    overflow: hidden;
  }
  .text-field .unit {
    position: absolute; right: 0; top: 0; width: 90px; height: 100%;
    background: var(--addon-bg); border-left: 2px solid var(--input-edge);
    display: flex; align-items: center; justify-content: center;
    color: var(--hint); font-size: 28px; font-weight: 300;
  }
  .text-field .placeholder {
    display: flex; align-items: center; justify-content: center; height: 100%;
    color: var(--placeholder); font-size: 31px; font-weight: 300; letter-spacing: 1px;
  }

  .confirm-button {
    position: absolute; left: 99px; top: 921px; width: 486px; height: 85px;
    background: var(--button-green); border-bottom: 4px solid var(--button-green-dark);
    border-radius: 4px; color: var(--white);
    font-size: 36px; font-weight: 400;
    display: flex; align-items: center; justify-content: center;
  }
</style>
</head>
<body>
  <div class="status-bar">
    <div class="carrier">
      <svg width="66" height="14" viewBox="0 0 66 14" aria-hidden="true">
        <circle cx="6" cy="7" r="5.5" fill="#fff"/>
        <circle cx="19" cy="7" r="5.5" fill="#fff"/>
        <circle cx="32" cy="7" r="5.5" fill="#fff"/>
        <circle cx="45" cy="7" r="5" fill="none" stroke="#fff" stroke-width="1.2"/>
        <circle cx="58" cy="7" r="5" fill="none" stroke="#fff" stroke-width="1.2"/>
      </svg>
      <span>NOVA</span>
      <svg width="26" height="20" viewBox="0 0 26 20" aria-hidden="true">
        <path d="M13 19 L1 6 A18 18 0 0 1 25 6 Z" fill="#fff"/>
      </svg>
    </div>
    <div class="time">4:21 PM</div>
    <div class="battery">
      <span>22%</span>
      <svg width="50" height="22" viewBox="0 0 50 22" aria-hidden="true">
        <rect x="1" y="1" width="42" height="20" rx="3" fill="none" stroke="#fff" stroke-width="2"/>
        <rect x="4" y="4" width="9" height="14" fill="#fff"/>
        <rect x="44" y="7" width="4" height="8" rx="1" fill="#fff"/>
      </svg>
    </div>
  </div>

  <header class="app-header">
    <div class="back-button">
      <svg width="26" height="40" viewBox="0 0 26 40" aria-label="Back">
        <path d="M21 4 L6 20 L21 36" fill="none" stroke="#fff" stroke-width="7" stroke-linecap="square"/>
      </svg>
    </div>
    <h1>Add Record</h1>
  </header>

  <p class="intro">Choose which category you<br>would like to add:</p>

  <section class="record-card">
    <div class="category-select">
      Weight
      <svg width="28" height="18" viewBox="0 0 28 18" aria-hidden="true">
        <path d="M3 3 L14 14 L25 3" fill="none" stroke="#fff" stroke-width="5"/>
      </svg>
    </div>

    <p class="field-label" style="top:190px;">Current weight</p>
    <div class="text-field" style="top:250px;">
      <span class="unit">kg</span>
    </div>

    <p class="field-label" style="top:378px;">Date of measurement</p>
    <div class="text-field" style="top:434px;">
      <span class="placeholder">DD/MM/YY</span>
    </div>
  </section>

  <div class="confirm-button">Confirm</div>
</body>
</html>
```